Spread for a luxury home magazine

- introduce owner and team with headshots and bios
- list benefits of choosing our title company
- luxury/elegant aesthetic

Will send more headshots and bios as things progress

```html
<!DOCTYPE html>
<html lang="en">
<head>
<meta charset="utf-8">
<title>Corvanne Title – Magazine Spread</title>
<link href="https://fonts.googleapis.com/css2?family=Libre+Baskerville:wght@400;700&family=Poppins:wght@300;400;500&display=swap" rel="stylesheet">
<style>
  :root {
    --backdrop: #6e6e6e;
    --ink: #070707;
    --gold: #b08d3a;
    --gold-light: #c9a55a;
    --white: #ffffff;
    --text: #e9e6df;
    --rule: rgba(176, 141, 58, 0.35);
    --serif: "Libre Baskerville", Georgia, serif;
    --sans: "Poppins", Arial, sans-serif;
  }
  * { box-sizing: border-box; margin: 0; padding: 0; }
  html, body { width: 1200px; height: 817px; overflow: hidden; background: var(--backdrop); }
  .spread {
    position: absolute; left: 66px; top: 94px; width: 1069px; height: 629px;
    background:
      radial-gradient(ellipse at 30% 20%, #1c1a17 0%, transparent 55%),
      radial-gradient(ellipse at 75% 70%, #191714 0%, transparent 55%),
      var(--ink);
    overflow: hidden; color: var(--text); font-family: var(--sans);
  }
  .spread > * { position: absolute; }
  .gutter { left: 566px; top: 0; width: 1px; height: 629px; background: rgba(255,255,255,0.04); }

  .owner-photo { left: 22px; top: 46px; width: 232px; height: 296px;
    background: linear-gradient(180deg, #3a2a20 0%, #5b4031 45%, #1a1412 100%); }

  .brand { left: 212px; top: 58px; width: 182px; text-align: center; }
  .brand-square { display: block; width: 22px; height: 22px; margin: 0 auto 30px; background: var(--gold); }
  .brand-name { font-family: var(--serif); font-weight: 400; font-size: 20px; color: var(--white); letter-spacing: 0.5px; }

  .rule { background: var(--gold); }
  .rule-top-h { left: 166px; top: 170px; width: 193px; height: 1px; }
  .rule-top-v { left: 358px; top: 170px; width: 1px; height: 18px; }
  .rule-bottom-h { left: 234px; top: 329px; width: 125px; height: 1px; }
  .rule-bottom-v { left: 358px; top: 314px; width: 1px; height: 15px; }

  .owner-name { left: 270px; top: 197px; font-family: var(--serif); font-weight: 400; font-size: 24px; line-height: 28px; color: var(--white); letter-spacing: 0.3px; }
  .owner-role { left: 270px; top: 226px; font-size: 11px; line-height: 12px; color: var(--gold); letter-spacing: 5px; font-weight: 300; }
  .owner-bio { left: 270px; top: 242px; width: 178px; font-size: 7px; line-height: 9.1px; color: var(--text); }

  .gold-block { left: 0; top: 342px; width: 198px; height: 287px; background: var(--gold); }
  .home-photo { left: 81px; top: 397px; width: 204px; height: 177px; border: 2px solid var(--white);
    background: linear-gradient(180deg, #8fa6a8 0%, #b7a792 40%, #6f6250 62%, #4d7a2d 78%, #3e6a24 100%); }

  .benefits-title { left: 236px; top: 350px; font-family: var(--serif); font-size: 13.5px; line-height: 16px; text-transform: uppercase; font-weight: 400; }
  .benefits-title span { display: block; }
  .line-white { color: var(--white); }
  .line-gold { color: var(--gold); }

  .service-group { left: 315px; width: 215px; }
  .service-group h3 { font-family: var(--serif); font-weight: 400; font-size: 8.4px; line-height: 10px; color: var(--gold-light); margin-bottom: 2px; }
  .service-group ul { list-style: none; }
  .service-group li { font-size: 5.3px; line-height: 6.6px; color: var(--white); padding-left: 6px; position: relative; }
  .service-group li::before { content: ""; position: absolute; left: 0; top: 2px; width: 3px; height: 3px; border-radius: 50%; background: var(--gold); }
  .group-property { top: 401px; }
  .group-realtor { top: 476px; }
  .group-coaching { top: 544px; }
  .service-divider { left: 315px; width: 215px; height: 1px; background: var(--rule); }
  .divider-1 { top: 470px; }
  .divider-2 { top: 538px; }

  .team-title { left: 652px; top: 60px; font-size: 16px; line-height: 18px; font-weight: 500; color: var(--gold); letter-spacing: 5.6px; }
  .member { left: 652px; width: 268px; }
  .member-name { font-family: var(--serif); font-weight: 700; font-size: 14.5px; color: var(--white); line-height: 18px; }
  .member-role { font-family: var(--serif); font-weight: 700; font-size: 9.5px; color: var(--gold); line-height: 12px; margin-bottom: 2px; }
  .member-bio { font-size: 6.6px; line-height: 8.2px; color: var(--text); }
  .member-1 { top: 94px; } .member-2 { top: 188px; } .member-3 { top: 290px; } .member-4 { top: 390px; } .member-5 { top: 493px; }
  .headshot { left: 929px; width: 92px; height: 93px; }
  .headshot-1 { top: 80px;  background: linear-gradient(160deg, #cfc8bd, #6e4b3a 60%, #1d1816); }
  .headshot-2 { top: 181px; background: linear-gradient(160deg, #9aa79a, #7a5a45 55%, #1f2326); }
  .headshot-3 { top: 282px; background: linear-gradient(160deg, #2b2522, #8a5b43 55%, #1a1412); }
  .headshot-4 { top: 384px; background: linear-gradient(160deg, #2a2623, #c9a57c 55%, #6a3a3a); }
  .headshot-5 { top: 486px; background: linear-gradient(160deg, #8a8f88, #d2aa78 55%, #3a2d25); }
  .team-divider { left: 652px; width: 277px; height: 1px; background: rgba(255,255,255,0.12); }
  .td-1 { top: 177px; } .td-2 { top: 278px; } .td-3 { top: 378px; } .td-4 { top: 479px; }

  .site-url { left: 652px; top: 582px; font-size: 8.6px; letter-spacing: 2.6px; color: var(--white); font-weight: 300; }
</style>
</head>
<body>
<main class="spread">
  <div class="gutter"></div>

  <div class="owner-photo" role="img" aria-label="Portrait of the founder, arms crossed, in a dark blazer"></div>

  <div class="brand">
    <span class="brand-square"></span>
    <span class="brand-name">Corvanne Title</span>
  </div>

  <div class="rule rule-top-h"></div>
  <div class="rule rule-top-v"></div>
  <div class="rule rule-bottom-h"></div>
  <div class="rule rule-bottom-v"></div>

  <h1 class="owner-name">ELENA R. NAVARRO</h1>
  <p class="owner-role">FOUNDER &amp; OWNER</p>
  <p class="owner-bio">Growing up in San Antonio, TX, Elena R. Navarro always knew she would work with people as building relationships always came naturally to her. This inherent interest in others led to her studies at Lone Star University where she earned a Bachelor of Science in Human Development and Family Studies.</p>

  <div class="gold-block"></div>
  <div class="home-photo" role="img" aria-label="Photo of a luxury stone home with a lit entry and landscaped lawn"></div>

  <h2 class="benefits-title"><span class="line-white">Benefits of choosing</span><span class="line-gold">our title company</span></h2>

  <section class="service-group group-property">
    <h3>Property Title Services</h3>
    <ul>
      <li>Condominiums</li><li>Lots &amp; acreage</li><li>Commercial land/unimproved</li><li>Farm &amp; ranch</li>
      <li>Single-family residential</li><li>Commercial property</li><li>Multi-family residential</li><li>Public/government-owned property</li>
    </ul>
  </section>
  <div class="service-divider divider-1"></div>
  <section class="service-group group-realtor">
    <h3>Realtor Title Services</h3>
    <ul>
      <li>Title Insurance</li><li>Escrow Services</li><li>Commercial Title Services</li><li>Underwriting &amp; Closing Coordination</li>
      <li>Sale/Leaseback Transactions</li><li>IRS Section 1031 Tax Deferred Exchanges</li><li>Reverse Mortgage, REO, and Foreclosure Services</li>
    </ul>
  </section>
  <div class="service-divider divider-2"></div>
  <section class="service-group group-coaching">
    <h3>Coaching Services</h3>
    <ul>
      <li>Business Coaching</li><li>Individual Coaching</li><li>Group Coaching</li><li>Team Development</li><li>Mentoring</li><li>Fulfillment Coaching</li>
    </ul>
  </section>

  <h2 class="team-title">CORVANNE TEAM</h2>

  <article class="member member-1">
    <h3 class="member-name">Clara Reyes</h3>
    <p class="member-role">Branch Manager/Escrow Officer</p>
    <p class="member-bio">I've been in Real Estate for over 10 years, starting as a marketing assistant for a real estate publication which grew into transaction coordinating and office managing. Those years of experiences allowed me to learn Commercial, Residential and Farm &amp; Ranch transactions like the back of my hand.</p>
  </article>
  <div class="team-divider td-1"></div>
  <article class="member member-2">
    <h3 class="member-name">Daniel Ortega</h3>
    <p class="member-role">Business Development</p>
    <p class="member-bio">I've been in Real Estate for over 10 years, starting as a marketing assistant for a real estate publication which grew into transaction coordinating and office managing. Those years of experiences allowed me to learn Commercial, Residential and Farm &amp; Ranch transactions like the back of my hand.</p>
  </article>
  <div class="team-divider td-2"></div>
  <article class="member member-3">
    <h3 class="member-name">Nina Hale</h3>
    <p class="member-role">Escrow Officer</p>
    <p class="member-bio">Recently moving from DFW, I have a hunger to grow my market in South Texas and San Antonio. Building my book of business and providing the best service in SA is my daily driver to get out of my comfort zone and generate new leads that will turn into life-long clients.</p>
  </article>
  <div class="team-divider td-3"></div>
  <article class="member member-4">
    <h3 class="member-name">Laura Vance</h3>
    <p class="member-role">Escrow Officer</p>
    <p class="member-bio">Recently moving from DFW, I have a hunger to grow my market in South Texas and San Antonio. Building my book of business and providing the best service in SA is my daily driver to get out of my comfort zone and generate new leads that will turn into life-long clients.</p>
  </article>
  <div class="team-divider td-4"></div>
  <article class="member member-5">
    <h3 class="member-name">Brooke Merrill</h3>
    <p class="member-role">Business Development</p>
    <p class="member-bio">Recently moving from DFW, I have a hunger to grow my market in South Texas and San Antonio. Building my book of business and providing the best service in SA is my daily driver to get out of my comfort zone and generate new leads that will turn into life-long clients.</p>
  </article>

  <div class="headshot headshot-1" role="img" aria-label="Headshot of Clara Reyes"></div>
  <div class="headshot headshot-2" role="img" aria-label="Headshot of Daniel Ortega"></div>
  <div class="headshot headshot-3" role="img" aria-label="Headshot of Nina Hale"></div>
  <div class="headshot headshot-4" role="img" aria-label="Headshot of Laura Vance"></div>
  <div class="headshot headshot-5" role="img" aria-label="Headshot of Brooke Merrill"></div>

  <p class="site-url">corvannetitle.com</p>
</main>
</body>
</html>
```